Kvtrpa@mailbox.test

I am making this a landing page and I want to really grab the person and get them to call. So, I want some up front language at the top language about why they should contact me right away. The person looking is in a tough spot, they woe a lot of debt, they do not want to file a bankruptcy for moral or personal reasons, I want them to know that bankruptcy is a legal process that can help them and that they should not fear checking out their options. I will give them all of the information and if they want to go further fine, if not, they will have a lot more information about their situation and options

The language at the top, I want to be

Thanks for visiting us. You came here because you are having debt problems and you want solutions. Yes, we want your business. But, we don't want it if it is not right for you. We have been at this a long time and assisted thousands of Hawaii people and families with their debt problems. Many of those people were referred by former clients, but, our biggest referral source is people who did not file a bankruptcy. The reason is simple- our absolutely free and confidential consultation will help you get a handle on your whole situation. We will discuss your assets, your debts, your income and expenses and get a complete picture. It is only with this complete global picture of your particular situation that you can know your options, all of them, and then you can decide what is right for you. You are the driver. Call us at 472-3000 (from all islands) and let us help you today!

The color should be calming without being wimpy.

i want the top to be simple and a call to action giving people the sense that we know what we are doing and that they can call us for truly no obligation and we can help them diagnose their money issues and I can give them their options and they can do whatever they wish with them.

Target Market(s)

Hawaii people between ages of 28-70 who have credit card, loan or mortgage problems and need a way to get out of their debt

Industry/Entity Type

Legal

Requirements
Must have
• Must incorporate the items at qalmeridge.com. May be helpful to look at sunwardledger.com for example of the "clean clear" landing I would like to "grab" the customer's attention and get them to call me, phone is better than email. So must have contact us too.

```html
<!DOCTYPE html>
<html lang="en">
<head>
<meta charset="utf-8">
<title>Hawaii Bankruptcy Attorney – Lionel K. Varden</title>
<link rel="stylesheet" href="https://fonts.googleapis.com/css2?family=Cinzel:wght@400;600&family=Open+Sans:wght@400;600;700&family=Arimo:wght@700&display=swap">
<style>
:root{
  --brown-dark:#3a3128;
  --brown-mid:#4d4236;
  --beige-top:#cfc6ab;
  --beige:#ddd6c0;
  --beige-light:#e6e1cf;
  --panel:#ebe7d9;
  --panel-edge:#d8d1bb;
  --text:#3b362e;
  --muted:#6f6757;
  --gold:#e9c46b;
  --white:#ffffff;
  --footer-text:#cfc7b3;
}
*{box-sizing:border-box;margin:0;padding:0}
html,body{width:1200px;height:1200px;overflow:hidden}
body{position:relative;font-family:"Open Sans",Arial,sans-serif;color:var(--text);
  background:linear-gradient(180deg,var(--beige-top) 0,var(--beige-top) 61px,var(--beige) 150px,var(--beige-light) 500px,var(--beige-light) 1080px)}
.header-band{position:absolute;left:0;top:61px;width:1200px;height:83px;background:linear-gradient(180deg,var(--brown-mid),var(--brown-dark))}
.tagline{position:absolute;font-family:"Cinzel",serif;color:var(--brown-dark);font-size:23px;letter-spacing:1px;line-height:1}
.tagline.primary{left:352px;top:8px}
.tagline.secondary{left:605px;top:32px}
.social{position:absolute;left:885px;top:6px;display:flex;gap:17px}
.social span{width:38px;height:38px;border-radius:5px;background:linear-gradient(180deg,#8b8170,#5d5446)}
.brand{position:absolute;left:123px;top:35px;width:217px;height:109px;background:linear-gradient(180deg,#efe9d8,#d8cfb6);
  display:flex;flex-direction:column;align-items:center;justify-content:center;font-family:"Cinzel",serif;color:var(--brown-mid);font-weight:400;text-align:center}
.brand .name{font-size:30px;line-height:1.05}
.brand .title{font-size:17px;margin-top:6px;letter-spacing:1px}
.call{position:absolute;left:893px;top:70px;font-family:"Arimo",Arial,sans-serif;font-weight:700;color:var(--gold);text-shadow:0 2px 2px rgba(0,0,0,.5)}
.call .label{font-size:26px;display:block}
.call .number{font-size:29px;display:block;margin-top:12px}
.hero{position:absolute;left:120px;top:152px;width:960px;height:299px;background:#efe9d8;padding:10px 11px}
.hero-photo{position:relative;width:938px;height:280px;
  background:linear-gradient(90deg,#b08a4e 0%,#8c7a63 22%,#cfd0cb 35%,#5b5e62 55%,#3e3e40 80%,#2c2c2d 100%)}
.hero-copy{position:absolute;left:471px;top:12px;width:462px;color:var(--white);font-weight:700;font-size:13.2px;line-height:17px;text-shadow:0 1px 1px rgba(0,0,0,.6)}
.hero-copy p{margin-bottom:17px}
.main-nav{position:absolute;left:120px;top:454px;width:960px;height:32px;background:linear-gradient(180deg,#514639,var(--brown-dark));border-radius:0 0 4px 4px;display:flex;align-items:center;padding-left:13px}
.main-nav a{font-size:12.5px;color:#e9e3d2;text-decoration:none;margin-right:30px;padding:4px 7px}
.main-nav a.current{background:#e6e0cd;color:var(--brown-dark)}
.sidebar{position:absolute;left:120px;top:510px;width:221px}
.side-heading{height:46px;background:linear-gradient(180deg,#5b4f42,var(--brown-dark));border-radius:0 12px 0 0;color:var(--white);font-size:23px;padding:6px 0 0 22px;box-shadow:0 2px 3px rgba(0,0,0,.3)}
.category-list{list-style:none;padding:12px 0 0 12px;height:228px}
.category-list li{font-size:12.5px;color:var(--muted);line-height:20px}
.category-list li::before{content:"›";margin-right:8px;color:var(--brown-dark);font-weight:700}
.consult-form{background:var(--panel);height:220px;padding:12px 9px 0}
.consult-form .field{display:block;height:20px;margin:0 0 10px;border:1px solid #c8c0a8;background:#e4dfcc;font-size:11px;color:var(--muted);padding:2px 8px}
.consult-form .field.message{height:70px;line-height:14px}
.submit{display:block;margin:12px 0 0 129px;width:72px;height:24px;background:var(--brown-dark);border:2px solid #b8ae94;color:var(--white);font-size:11px;letter-spacing:1px;text-align:center;line-height:20px}
.content{position:absolute;left:355px;top:514px;width:722px;height:537px;background:var(--panel);border-radius:10px;border:1px solid var(--panel-edge);padding:14px 16px;font-size:14px;line-height:24px;color:var(--text)}
.content p{margin-bottom:18px}
.footer{position:absolute;left:0;top:1080px;width:1200px;height:120px;background:linear-gradient(180deg,#4a4034,#2f2821)}
.footer-links{position:absolute;left:131px;top:10px;font-size:12px;color:var(--footer-text)}
.footer-links span{margin:0 7px}
.copyright{position:absolute;left:131px;top:34px;font-size:10px;color:var(--footer-text)}
.contact-info{position:absolute;left:832px;top:8px;color:var(--footer-text);font-size:12.5px;line-height:17px}
.contact-info h3{font-size:17px;font-weight:400;color:var(--white);margin-bottom:2px}
.contact-info .email{color:var(--white)}
</style>
</head>
<body>
<div class="header-band"></div>
<div class="tagline primary">HAWAII BANKRUPTCY ATTORNEY</div>
<div class="tagline secondary">BEST DEBT SOLUTIONS</div>
<div class="social" aria-label="Social links"><span></span><span></span><span></span><span></span></div>
<div class="brand"><span class="name">LIONEL K.<br>VARDEN</span><span class="title">ATTORNEY-AT-LAW</span></div>
<div class="call"><span class="label">CALL:</span><span class="number">808-472-3000</span></div>

<section class="hero">
  <div class="hero-photo" role="img" aria-label="Photo of a man in a shirt and tie in a wheat field holding out his empty trouser pockets">
    <div class="hero-copy">
      <p>Thanks for visiting us.<br>You came here because you are having debt problems and you want solutions. Yes, we want your business. But, we don't want it if it is not right for you. We have been at this a long time and assisted thousands of Hawaii people and families with their debt problems.</p>
      <p>The reason is simple- our absolutely free and confidential consultation will help you get a handle on your whole situation. We will discuss your assets, your debts, your income and expenses and get a complete picture. It is only with this complete global picture of your particular situation that you can know your options, all of them, and then you can decide what is right for</p>
      <p>You are the driver. Call us at<br>808-472-3000 (from all islands) and let us help you today!</p>
    </div>
  </div>
</section>

<nav class="main-nav">
  <a>HOME</a><a class="current">ABOUT US</a><a>CHAPTER 7 BANKRUPTCY</a><a>CHAPTER 13 BANKRUPTCY</a><a>BLOG</a><a>CONTACT US</a>
</nav>

<aside class="sidebar">
  <div class="side-heading">Categories</div>
  <ul class="category-list">
    <li>Articles</li><li>bankruptcy</li><li>Bankruptcy Hawaii</li><li>Bankruptcy Honolulu</li><li>bankruptcy oahu</li><li>Blog</li><li>Blogroll</li><li>Care</li><li>Chapter 13</li><li>Chapter 13 Bankruptcy Hawaii</li>
  </ul>
  <div class="side-heading">Free Consultation</div>
  <form class="consult-form">
    <span class="field">Name :</span>
    <span class="field">Email :</span>
    <span class="field">Phone :</span>
    <span class="field message">Briefly describe your legal issue here.</span>
    <span class="submit">SUBMIT</span>
  </form>
</aside>

<main class="content">
  <p>Thanks for visiting us.</p>
  <p>You came here because you are having debt problems and you want solutions.</p>
  <p>Yes, we want your business.</p>
  <p>But, we don't want it if it is not right for you. We have been at this a long time and assisted thousands of Hawaii people and families with their debt problems.</p>
  <p>Many of those people were referred by former clients, but, our biggest referral source is people who did not file a bankruptcy.</p>
  <p>The reason is simple- our absolutely free and confidential consultation will help you get a handle on your whole situation.</p>
  <p>We will discuss your assets, your debts, your income and expenses and get a complete picture. It is only with this complete global picture of your particular situation that you can know your options, all of them, and then you can decide what is right for you.</p>
  <p>You are the driver. Call us at<br>808-472-3000 (from all islands) and let us help you today!</p>
</main>

<footer class="footer">
  <div class="footer-links">Home<span>|</span>About Us<span>|</span>Chapter 7 Bankruptcy<span>|</span>Chapter 13 Bankruptcy<span>|</span>Blog<span>|</span>Contact Us</div>
  <div class="copyright">© copy right 2012 by qalmeridge.com All rights reserved.</div>
  <div class="contact-info">
    <h3>Contact Info</h3>
    Lionel K. Varden, Attorney-at-Law<br>
    740 Harbor Row Suite 1410<br>
    Honolulu, HI 96813<br>
    808-472-3000<br>
    <span class="email">info@qalmeridge.com</span>
  </div>
</footer>
</body>
</html>
```